Need a book cover design for a Lumora Book on Herbal Remedies

I need a book cover for my new ebook, here are the details:
Title: Meadow Cures
Sub-Heading: Buried Ancient Garden Tonics
Reclaiming the Wisdom of Roots for Everyday Wellness and Strength
Author: Nora Belcourt

```html
<!DOCTYPE html>
<html lang="en">
<head>
<meta charset="utf-8">
<title>Meadow Cures — Book Cover</title>
<link rel="stylesheet" href="https://fonts.googleapis.com/css2?family=Londrina+Solid:wght@400;900&family=Poppins:wght@700&display=swap">
<style>
  :root {
    --page: #ffffff;
    --stone-light: #dfe1dc;
    --stone-mid: #c4c8c0;
    --sage-green: rgba(104, 170, 60, 0.85);
    --lavender: rgba(120, 100, 190, 0.75);
    --petal-pink: rgba(228, 90, 170, 0.7);
    --amber: rgba(200, 110, 40, 0.85);
    --cinnamon: rgba(140, 80, 50, 0.85);
    --oil-gold: rgba(210, 190, 80, 0.75);
    --chamomile: rgba(235, 232, 210, 0.85);
    --copper: rgba(170, 110, 80, 0.7);
    --mint: rgba(110, 190, 70, 0.8);
    --calendula: rgba(245, 160, 30, 0.85);
    --hypericum: rgba(220, 200, 40, 0.85);
    --thistle: rgba(170, 80, 160, 0.6);
    --bowl-brown: rgba(120, 90, 65, 0.75);
    --title-green: #3f9a1e;
    --deep-green: #1f4a12;
  }
  html, body {
    margin: 0;
    padding: 0;
    width: 1200px;
    height: 1200px;
    overflow: hidden;
    background: var(--page);
  }
  .canvas {
    position: relative;
    width: 1200px;
    height: 1200px;
  }
  .cover {
    position: absolute;
    left: 244px;
    top: 50px;
    width: 712px;
    height: 1068px;
    overflow: hidden;
  }
  .cover-photo {
    position: absolute;
    inset: 0;
    background:
      radial-gradient(ellipse 150px 130px at 70px 80px, var(--sage-green), transparent 75%),
      radial-gradient(ellipse 110px 170px at 300px 200px, var(--lavender), transparent 75%),
      radial-gradient(ellipse 70px 60px at 280px 100px, var(--petal-pink), transparent 75%),
      radial-gradient(ellipse 80px 60px at 490px 70px, rgba(200, 190, 235, 0.8), transparent 75%),
      radial-gradient(ellipse 120px 160px at 640px 140px, var(--amber), transparent 75%),
      radial-gradient(ellipse 110px 140px at 540px 220px, var(--petal-pink), transparent 75%),
      radial-gradient(ellipse 80px 110px at 650px 360px, rgba(190, 160, 110, 0.7), transparent 75%),
      radial-gradient(ellipse 70px 90px at 30px 390px, var(--oil-gold), transparent 75%),
      radial-gradient(ellipse 110px 180px at 70px 580px, var(--cinnamon), transparent 75%),
      radial-gradient(ellipse 120px 150px at 670px 580px, var(--mint), transparent 75%),
      radial-gradient(ellipse 80px 70px at 610px 640px, var(--calendula), transparent 75%),
      radial-gradient(ellipse 90px 80px at 680px 720px, rgba(230, 190, 90, 0.7), transparent 75%),
      radial-gradient(ellipse 130px 150px at 60px 790px, var(--chamomile), transparent 70%),
      radial-gradient(ellipse 150px 170px at 60px 790px, var(--copper), transparent 80%),
      radial-gradient(ellipse 140px 120px at 120px 980px, var(--bowl-brown), transparent 75%),
      radial-gradient(ellipse 140px 110px at 330px 1000px, rgba(160, 130, 110, 0.75), transparent 75%),
      radial-gradient(ellipse 60px 60px at 390px 920px, rgba(110, 50, 30, 0.7), transparent 75%),
      radial-gradient(ellipse 90px 80px at 530px 850px, var(--thistle), transparent 75%),
      radial-gradient(ellipse 220px 260px at 620px 900px, var(--hypericum), transparent 75%),
      radial-gradient(ellipse 260px 300px at 600px 960px, rgba(90, 140, 50, 0.7), transparent 80%),
      radial-gradient(ellipse 62% 52% at 50% 52%, var(--stone-light) 0%, var(--stone-mid) 100%);
  }
  .cover-text {
    position: absolute;
    inset: 0;
    text-align: center;
  }
  .title {
    position: absolute;
    left: 0;
    right: 0;
    top: 293px;
    margin: 0;
    font-family: "Londrina Solid", "Arial Narrow", sans-serif;
    font-weight: 900;
    font-size: 172px;
    line-height: 140px;
    letter-spacing: 0;
    color: var(--title-green);
    text-transform: uppercase;
    transform: scale(0.94, 1.2);
    transform-origin: 50% 0;
  }
  .title span { display: block; }
  .subtitle {
    position: absolute;
    left: 0;
    right: 0;
    top: 670px;
    margin: 0;
    font-family: "Londrina Solid", "Arial Narrow", sans-serif;
    font-weight: 400;
    font-size: 34px;
    line-height: 36px;
    color: var(--deep-green);
    text-transform: uppercase;
    padding-right: 14px;
  }
  .tagline {
    position: absolute;
    left: 120px;
    right: 134px;
    top: 706px;
    margin: 0;
    font-family: "Poppins", Arial, sans-serif;
    font-weight: 700;
    font-size: 16.5px;
    line-height: 22px;
    color: var(--deep-green);
    text-transform: uppercase;
  }
  .author {
    position: absolute;
    left: 0;
    right: 0;
    top: 796px;
    margin: 0;
    font-family: "Londrina Solid", "Arial Narrow", sans-serif;
    font-weight: 900;
    font-size: 48px;
    line-height: 50px;
    color: var(--deep-green);
    text-transform: uppercase;
    padding-right: 14px;
  }
</style>
</head>
<body>
  <div class="canvas">
    <section class="cover">
      <div class="cover-photo" role="img" aria-label="Overhead photo of herbs and remedies on grey stone: mortar with sage, lavender sprigs, echinacea, rose petals, amber oil bottles, cinnamon sticks, chamomile, mint, calendula, star anise, milk thistle and yellow wildflowers framing the centre"></div>
      <div class="cover-text">
        <h1 class="title"><span>Meadow</span><span>Cures</span></h1>
        <p class="subtitle">Buried Ancient Garden Tonics</p>
        <p class="tagline">Reclaiming the Wisdom of Roots for Everyday Wellness and Strength</p>
        <p class="author">Nora Belcourt</p>
      </div>
    </section>
  </div>
</body>
</html>
```